Business Card Designs

Looking to design a 3.5" x 2" standard business card for our employees.
The design needs to be sleek, simple, and modern. We would like our logo (attached) to be incorporated, but not in that colour, rather an outline of the logo in either gold or silver (whichever looks better).

Modern and Simple is what we are looking for, but be creative in incorporating the logo.

```html
<!DOCTYPE html>
<html lang="en">
<head>
<meta charset="utf-8">
<title>Business Card – Front and Back</title>
<link href="https://fonts.googleapis.com/css2?family=Raleway:wght@400;500;600&display=swap" rel="stylesheet">
<style>
  :root {
    --page: #ececec;
    --card: #ffffff;
    --card-fade: #f6f6f6;
    --gold: #c2a468;
    --gold-light: #ead8b4;
    --gold-deep: #b8975a;
    --ink: #1c1c1c;
    --rule: #9a9a9a;
  }
  * { box-sizing: border-box; margin: 0; padding: 0; }
  html, body {
    width: 1200px; height: 1200px; overflow: hidden;
    background: var(--page);
    font-family: "Raleway", "Helvetica Neue", Arial, sans-serif;
  }
  .sheet {
    width: 1200px; height: 1200px;
    display: flex; flex-direction: column; align-items: center; justify-content: center;
    gap: 60px;
  }
  .card {
    position: relative;
    width: 900px; height: 514px;
    border-radius: 34px;
    background: linear-gradient(180deg, var(--card) 55%, var(--card-fade));
    box-shadow: 0 6px 22px rgba(0,0,0,.12);
    overflow: hidden;
  }
  .gold-band {
    position: absolute; bottom: 0; height: 34px;
    background: linear-gradient(90deg, var(--gold-deep), var(--gold) 35%, var(--gold-light) 62%, var(--gold) 85%, var(--gold-deep));
    clip-path: polygon(18px 0, 100% 0, 100% 100%, 0 100%);
  }
  .card--front .gold-band { left: 470px; right: 120px; }
  .card--back .gold-band { left: 470px; right: 120px; }

  /* front */
  .contact {
    position: absolute; left: 110px; top: 168px;
  }
  .contact__head {
    position: relative; padding-left: 26px; margin-bottom: 26px;
  }
  .contact__head::before {
    content: ""; position: absolute; left: 0; top: 8px; bottom: 4px; width: 9px;
    background: linear-gradient(180deg, var(--gold-light), var(--gold-deep));
  }
  .contact__name {
    font-size: 50px; font-weight: 600; letter-spacing: 1px; color: var(--gold); line-height: 1;
  }
  .contact__role {
    font-size: 24px; font-weight: 500; color: var(--ink); margin-top: 6px; letter-spacing: .5px;
  }
  .contact__list { list-style: none; }
  .contact__item {
    display: flex; align-items: center; gap: 18px;
    font-size: 27px; color: var(--ink); margin-bottom: 12px; letter-spacing: .4px;
  }
  .contact__icon { width: 28px; height: 28px; flex: none; }
  .divider {
    position: absolute; left: 450px; top: 150px; width: 1px; height: 200px; background: var(--rule);
  }
  .brand {
    position: absolute; display: flex; align-items: center; color: var(--gold);
    font-weight: 600; letter-spacing: 3px; text-transform: uppercase;
  }
  .brand__mark { background: var(--gold); flex: none; }
  .card--front .brand { left: 520px; top: 232px; font-size: 28px; gap: 14px; }
  .card--front .brand__mark { width: 20px; height: 20px; }
  .card--back .brand { left: 0; right: 0; top: 222px; justify-content: center; font-size: 52px; gap: 24px; }
  .card--back .brand__mark { width: 36px; height: 36px; }
</style>
</head>
<body>
<main class="sheet">
  <section class="card card--front" aria-label="Card front">
    <div class="contact">
      <div class="contact__head">
        <h1 class="contact__name">JOHN DOE</h1>
        <p class="contact__role">CEO | FOUNDER</p>
      </div>
      <ul class="contact__list">
        <li class="contact__item">
          <svg class="contact__icon" viewBox="0 0 24 24"><path fill="#c2a468" d="M6.6 10.8a15 15 0 0 0 6.6 6.6l2.2-2.2a1 1 0 0 1 1-.25 11.4 11.4 0 0 0 3.6.57 1 1 0 0 1 1 1V20a1 1 0 0 1-1 1A17 17 0 0 1 3 4a1 1 0 0 1 1-1h3.5a1 1 0 0 1 1 1c0 1.25.2 2.45.57 3.57a1 1 0 0 1-.25 1z"/></svg>
          (000) 000 0000
        </li>
        <li class="contact__item">
          <svg class="contact__icon" viewBox="0 0 24 24"><rect x="2" y="5" width="20" height="14" fill="#c2a468"/><path d="M2 5l10 8 10-8" fill="none" stroke="#fff" stroke-width="1.5"/></svg>
          email@youremail.com
        </li>
        <li class="contact__item">
          <svg class="contact__icon" viewBox="0 0 24 24" fill="none" stroke="#c2a468" stroke-width="1.6"><circle cx="12" cy="12" r="10"/><ellipse cx="12" cy="12" rx="4.5" ry="10"/><path d="M2 12h20M4 7h16M4 17h16"/></svg>
          www.yourwebsite.com
        </li>
      </ul>
    </div>
    <div class="divider"></div>
    <div class="brand"><span class="brand__mark"></span>Harbourline Suites</div>
    <div class="gold-band"></div>
  </section>

  <section class="card card--back" aria-label="Card back">
    <div class="brand"><span class="brand__mark"></span>Harbourline Suites</div>
    <div class="gold-band"></div>
  </section>
</main>
</body>
</html>
```